Referral Club PostCard/ Index Card

I need to create an Index card for a Contractor Referral Club. I already did my own door hanger which I can show you. Cost is a factor because I'm just starting my company. You guys have already created my 2 logos when I did a previous logo project so I want to use those logos and colors to create a scheme double sided postcard for my referral club attached to our some examples of other ones I've seen. So, you can 1 of 3 different design/color schemes as a basis:
1) The Black background with Blue Shield
2). The Light Blue background with the white wave (Really like this and the black one)
3). My White background blue/black business card design.
So, 3 different design/color schemes to attack?

You can also look at my website for ideas

http://www.TheDwellingCounselor.example
Updates

I have a picture of the things I want to say on BOTH sides on the Index card/[Post card. Basically, there are two versions that can be created, one with the black background/blue logo motif or one with the white/blue background logo. I bought BOTH designs in my logo contest. Actually 1 is the front of the cards and the other is the back of my card. I'm looking for creativity to get these contractors to join this referral club so I can get more leads.

Need extra days to review

I have some new logos,, icons and pdfs to submit for consideration

Target Market(s)

Drawing Other Contractors into my Professional Referral Exchange Club

Industry/Entity Type

Public Insurance Adjusting

Font styles to use
Serif
Sans Serif
Other font styles liked:
• Love Zurich font but very few people have it..It is eye drawing!!

Colors
0054AA
0677BA
7BADD7
CADEEF
E8F1F8
0094D4
00A9DD
6FCCEA
C7EBF8
E9F6FB
EE7325
F08F49
F5BC92
FAE3D3
FDF4ED

Requirements
Must have
• My Blue or Black/White color scheme to stay consistent to what Ive already had done
Nice to have
• Something that jumps off to entice them to join that I haven't thought of.

```html
<!DOCTYPE html>
<html lang="en">
<head>
<meta charset="utf-8">
<title>The Dwelling Counselor – Referral Exchange Club Card</title>
<link rel="stylesheet" href="https://fonts.googleapis.com/css2?family=Oswald:wght@300;400;500&display=swap">
<style>
  :root {
    --black: #000000;
    --wave-grey: #2c3238;
    --brand-blue: #0677ba;
    --deep-blue: #0054aa;
    --orange: #e07b0c;
    --white: #ffffff;
    --soft-white: #eef2f6;
  }
  * { box-sizing: border-box; margin: 0; padding: 0; }
  html, body { width: 1200px; height: 1200px; overflow: hidden; background: var(--white); }
  body { position: relative; font-family: "Oswald", "Arial Narrow", sans-serif; }

  .card { position: absolute; overflow: hidden; }
  .card--front { left: 154px; top: 23px; width: 876px; height: 509px; background: var(--black); }
  .card--back { left: 160px; top: 612px; width: 873px; height: 512px; }

  .waves { position: absolute; inset: 0; width: 100%; height: 100%; }

  .brand { position: absolute; left: 0; right: 0; top: 120px; text-align: center; }
  .brand__mark { display: block; width: 26px; height: 26px; margin: 0 auto 16px; background: var(--brand-blue); }
  .brand__name { font-weight: 500; font-size: 40px; letter-spacing: 2px; color: var(--brand-blue); line-height: 1; }

  .orange-bar { position: absolute; height: 35px; background: var(--orange); }
  .orange-bar--left { left: 0; top: 318px; width: 178px; border-radius: 0 4px 4px 0; }
  .orange-bar--right { right: 0; top: 318px; width: 179px; border-radius: 4px 0 0 4px; }

  .club-title { position: absolute; left: 0; right: 0; top: 304px; text-align: center; font-weight: 400; font-size: 49px; line-height: 1.3; color: var(--brand-blue); letter-spacing: -0.5px; }
  .club-tagline { position: absolute; left: 0; right: 0; top: 415px; text-align: center; font-weight: 400; font-size: 42px; line-height: 1.2; color: var(--soft-white); letter-spacing: -0.5px; }

  .scene-fill { position: absolute; inset: 0;
    background:
      radial-gradient(ellipse at 78% 40%, rgba(150,160,165,0.55), transparent 45%),
      radial-gradient(ellipse at 50% 85%, rgba(0,84,170,0.55), transparent 50%),
      linear-gradient(120deg, #2a2420 0%, #3d352c 35%, #4a4b4d 60%, #6f6356 80%, #3a2c22 100%); }
  .scene-shade { position: absolute; inset: 0; background: rgba(0,0,0,0.3); }

  .reasons-head { position: absolute; left: 26px; top: 36px; display: flex; align-items: center; }
  .reasons-head__bar { width: 77px; height: 34px; background: var(--orange); border-radius: 3px; }
  .reasons-head__title { margin-left: 22px; font-weight: 400; font-size: 44px; line-height: 1.3; color: var(--white); letter-spacing: -0.5px; }

  .social { position: absolute; top: 43px; display: block; width: 57px; height: 57px; border-radius: 50%; background: var(--white); }
  .social--one { left: 677px; }
  .social--two { left: 748px; }

  .reasons { position: absolute; left: 25px; top: 133px; list-style: none; }
  .reasons li { font-weight: 400; font-size: 24.5px; line-height: 40px; color: var(--white); letter-spacing: -0.6px; }
  .reasons u { text-underline-offset: 3px; }

  .services { position: absolute; left: 594px; top: 130px; list-style: none; }
  .services li { display: flex; align-items: center; height: 34.7px; font-weight: 400; font-size: 21.5px; color: var(--soft-white); letter-spacing: -0.4px; }
  .services li::before { content: ""; width: 19px; height: 19px; margin-right: 10px; background: var(--orange); border-radius: 2px; }

  .call { position: absolute; left: 18px; top: 344px; display: flex; align-items: center; }
  .call__icon { width: 85px; height: 85px; border-radius: 50%; background: var(--white); display: flex; align-items: center; justify-content: center; }
  .call__text { margin-left: 20px; font-weight: 400; font-size: 64px; line-height: 1; color: var(--white); letter-spacing: -1.5px; white-space: nowrap; }

  .closing { position: absolute; left: 25px; top: 454px; font-weight: 400; font-size: 31px; line-height: 1.3; color: var(--white); letter-spacing: -0.8px; white-space: nowrap; }
</style>
</head>
<body>

<section class="card card--front">
  <svg class="waves" viewBox="0 0 876 509" preserveAspectRatio="none" aria-hidden="true">
    <path d="M0 360 C180 345 330 430 520 385 C660 350 760 285 876 290 L876 509 L0 509 Z" fill="var(--wave-grey)"/>
    <path d="M0 410 C150 470 300 470 460 430 C620 390 760 390 876 405 L876 440 C740 430 600 455 450 488 C300 515 140 505 0 450 Z" fill="var(--black)"/>
  </svg>
  <div class="brand">
    <span class="brand__mark"></span>
    <p class="brand__name">THE DWELLING COUNSELOR</p>
  </div>
  <div class="orange-bar orange-bar--left"></div>
  <div class="orange-bar orange-bar--right"></div>
  <h1 class="club-title">REFERAL EXCHANGE CLUB</h1>
  <p class="club-tagline">BEST ON THE SOUTH SINCE 2010</p>
</section>

<section class="card card--back">
  <div class="scene-fill" role="img" aria-label="Photo of a fire-damaged house interior"></div>
  <div class="scene-shade"></div>
  <svg class="waves" viewBox="0 0 873 512" preserveAspectRatio="none" aria-hidden="true">
    <path d="M0 430 C200 380 420 470 620 420 C740 390 820 400 873 410 L873 512 L0 512 Z" fill="rgba(44,50,56,0.55)"/>
  </svg>

  <div class="reasons-head">
    <span class="reasons-head__bar"></span>
    <h2 class="reasons-head__title">THE REASONS TO BE IN CLUB</h2>
  </div>
  <span class="social social--one"></span>
  <span class="social social--two"></span>

  <ol class="reasons">
    <li>1 CONSECTETUR NULLA PROIDENT VOLUPTATE IRURE.</li>
    <li>2 GUARANTED RETURN REFERAL <u>something</u></li>
    <li>3 $75 GIFT <u>SOMETHING</u></li>
    <li>4 TRUST YOUR CLIENT</li>
  </ol>

  <ul class="services">
    <li>Hurricane Damage Claims</li>
    <li>Water Damage Claims</li>
    <li>Wind Damage Claims</li>
    <li>Roof Damage Claims</li>
    <li>Flood Damage Claims</li>
    <li>Fire Damage Claims</li>
    <li>Mold Growth/Damage Claims</li>
    <li>Hail Damage Claims</li>
  </ul>

  <div class="call">
    <span class="call__icon">
      <svg width="50" height="50" viewBox="0 0 24 24" aria-hidden="true">
        <path fill="var(--orange)" d="M6.6 10.8c1.4 2.8 3.8 5.1 6.6 6.6l2.2-2.2c.3-.3.7-.4 1-.2 1.1.4 2.3.6 3.6.6.6 0 1 .4 1 1V20c0 .6-.4 1-1 1C10.6 21 3 13.4 3 4c0-.6.4-1 1-1h3.5c.6 0 1 .4 1 1 0 1.3.2 2.5.6 3.6.1.3 0 .7-.2 1z"/>
      </svg>
    </span>
    <p class="call__text">CALL 850-555-0137</p>
  </div>

  <p class="closing">OCCAECAT, EXERCITATION IN EU DESERUNT SUNT, DOLOR MOLLIT AD SINT.</p>
</section>

</body>
</html>
```